Footwear Retail Chain Store Needs New Design for Display Clip

We have several retail shoe stores in Canada. As part of our display of boots, we identify our boots that are waterproof, so that customers can easily obtain information.

What we require:

- We need a design to be printed on a plastic clip of the exact dimensions as in the attachment with the intent of advising consumers which boots are WATERPROOF;
- The utility of the clip is to place it on boots that are displayed to the consumers in the stores;
- We want a design where we are advising consumers that the boot is WATERPROOF – we want a design that is different from the attached pictures (as there may be copyright issues with the image);
- The word “WATERPROOF” should be visible clearly on the clip;
- Despite the word being there, the design on its own should reflect the concept of waterproof without even having to read the word.

Then, we want the exact same design, except that the word "waterproof" should be changed to "Water Resistant".

Target Market(s)

The clip will be placed on all various sorts of boots, for all types and age group of customers.

Industry/Entity Type

Store

Requirements
Must have
• - A very nice image in the background of the clip that symbolizes waterproof;
• - the words "waterproof" or "water resistant" on the front

```html
<!DOCTYPE html>
<html lang="en">
<head>
<meta charset="UTF-8">
<title>Boot Display Clips – Water Resistant &amp; Waterproof</title>
<link rel="stylesheet" href="https://fonts.googleapis.com/css2?family=Russo+One&display=swap">
<style>
  :root {
    --page: #ffffff;
    --clip-blue: #1d4fe6;
    --splash-light: #bfe6f7;
    --splash-mid: #6fb4e6;
    --splash-deep: #2a63d8;
    --type-white: #ffffff;
    --shadow-navy: #0b1c78;
    --shadow-ice: #a9dcf4;
    --edge: #c9d3e6;
  }
  * { margin: 0; padding: 0; box-sizing: border-box; }
  html, body {
    width: 1200px;
    height: 592px;
    overflow: hidden;
    background: var(--page);
  }
  .canvas {
    position: relative;
    width: 1200px;
    height: 592px;
  }
  .clip {
    position: absolute;
    top: 38px;
    width: 516px;
    height: 516px;
    background: var(--clip-blue);
    outline: 1px solid var(--edge);
    overflow: hidden;
  }
  .clip--resistant { left: 69px; }
  .clip--waterproof { left: 613px; }

  .splash {
    position: absolute;
    filter: blur(2px);
  }
  .splash--top {
    left: 290px; top: 12px; width: 240px; height: 150px;
    border-radius: 60% 40% 45% 70% / 55% 45% 60% 50%;
    background: radial-gradient(ellipse at 65% 45%, var(--splash-light) 0%, var(--splash-mid) 45%, rgba(111,180,230,0) 75%);
  }
  .splash--wave {
    left: -20px; top: 345px; width: 290px; height: 190px;
    border-radius: 70% 30% 40% 50% / 60% 40% 50% 40%;
    background: radial-gradient(ellipse at 30% 55%, var(--splash-light) 0%, var(--splash-mid) 40%, rgba(42,99,216,0) 75%);
  }
  .splash--corner {
    left: 320px; top: 400px; width: 220px; height: 140px;
    border-radius: 60% 40% 0 0 / 70% 50% 0 0;
    background: radial-gradient(ellipse at 65% 80%, var(--splash-light) 0%, var(--splash-mid) 45%, rgba(111,180,230,0) 78%);
  }
  .splash--stream {
    left: 60px; top: 300px; width: 360px; height: 70px;
    border-radius: 50%;
    transform: rotate(-10deg);
    background: radial-gradient(ellipse at 45% 55%, rgba(191,230,247,0.85) 0%, rgba(111,180,230,0.5) 40%, rgba(111,180,230,0) 72%);
  }

  .wordmark {
    position: absolute;
    inset: 0;
    width: 516px;
    height: 516px;
  }
  .wordmark text {
    font-family: "Russo One", "Arial Black", sans-serif;
    fill: var(--type-white);
  }
  .wordmark--resistant text {
    filter: drop-shadow(-7px -6px 0 var(--shadow-navy));
  }
  .wordmark--waterproof text {
    filter: drop-shadow(4px 7px 0 var(--shadow-ice));
  }
</style>
</head>
<body>
<main class="canvas">

  <section class="clip clip--resistant" aria-label="Water resistant boot clip">
    <div class="splash splash--top" role="img" aria-label="Photo of a water splash spraying in the top right"></div>
    <div class="splash splash--wave" role="img" aria-label="Photo of a curling wave of water in the lower left"></div>
    <div class="splash splash--corner" role="img" aria-label="Photo of splashing water in the lower right corner"></div>
    <svg class="wordmark wordmark--resistant" viewBox="0 0 516 516" aria-label="Water Resistant">
      <text x="79" y="250" font-size="112" textLength="357" lengthAdjust="spacingAndGlyphs">WATER</text>
      <text x="79" y="350" font-size="68" textLength="357" lengthAdjust="spacingAndGlyphs">RESISTANT</text>
    </svg>
  </section>

  <section class="clip clip--waterproof" aria-label="Waterproof boot clip">
    <div class="splash splash--top" role="img" aria-label="Photo of a water splash spraying in the top right"></div>
    <div class="splash splash--stream" role="img" aria-label="Photo of a thin stream of water droplets crossing the middle"></div>
    <div class="splash splash--wave" role="img" aria-label="Photo of a curling wave of water in the lower left"></div>
    <div class="splash splash--corner" role="img" aria-label="Photo of splashing water in the lower right corner"></div>
    <svg class="wordmark wordmark--waterproof" viewBox="0 0 516 516" aria-label="Waterproof">
      <text x="27" y="280" font-size="68" textLength="460" lengthAdjust="spacingAndGlyphs">WATERPROOF</text>
    </svg>
  </section>

</main>
</body>
</html>
```